Tirovel

We need a business card for our company is a holding for different business all are different we try to have some air of relax and fun in our projects we add pictures of the office to give you an idea od the mood of the business

Business

```html
<!DOCTYPE html>
<html lang="en">
<head>
<meta charset="utf-8">
<title>Tirovel Business Card</title>
<link rel="stylesheet" href="https://fonts.googleapis.com/css2?family=Roboto:wght@300;400;700&display=swap">
<style>
  :root {
    --page-bg: #e9e7e3;
    --card-bg: #ffffff;
    --brand-yellow: #f4e629;
    --brand-brown: #5b3b1e;
    --ink: #4a4038;
    --ink-soft: #6f665e;
  }
  * { box-sizing: border-box; margin: 0; padding: 0; }
  html, body {
    width: 1200px;
    height: 828px;
    overflow: hidden;
    background: var(--page-bg);
    font-family: "Roboto", Arial, sans-serif;
  }
  .canvas {
    position: relative;
    width: 1200px;
    height: 828px;
  }
  .card {
    position: absolute;
    width: 520px;
    height: 300px;
    background: var(--card-bg);
    box-shadow: 0 6px 18px rgba(0,0,0,0.12);
    overflow: hidden;
  }
  .card--front { left: 60px; top: 130px; }
  .card--back  { left: 620px; top: 398px; }

  .brand {
    display: flex;
    align-items: center;
    gap: 10px;
  }
  .brand__dot {
    width: 34px;
    height: 34px;
    border-radius: 50%;
    background: var(--brand-yellow);
  }
  .brand__name {
    font-weight: 700;
    color: var(--brand-brown);
    letter-spacing: -0.5px;
  }
  .card--front .brand {
    position: absolute;
    left: 50%;
    top: 50%;
    transform: translate(-50%, -50%);
  }
  .card--front .brand__name { font-size: 48px; }
  .card--front .brand__dot { width: 44px; height: 44px; }

  .card--back .brand {
    position: absolute;
    left: 34px;
    top: 38px;
  }
  .card--back .brand__name { font-size: 34px; }

  .person {
    position: absolute;
    right: 34px;
    top: 40px;
    text-align: right;
    color: var(--ink);
  }
  .person__name {
    font-size: 13px;
    font-weight: 400;
    letter-spacing: 1.2px;
  }
  .person__title {
    font-size: 9px;
    font-weight: 300;
    color: var(--ink-soft);
    margin-top: 2px;
  }
  .address {
    position: absolute;
    right: 34px;
    top: 104px;
    text-align: right;
    font-size: 10px;
    line-height: 1.5;
    color: var(--ink);
    font-weight: 300;
  }
  .contacts {
    position: absolute;
    left: 34px;
    top: 160px;
    list-style: none;
    font-size: 11px;
    color: var(--ink);
    font-weight: 300;
  }
  .contacts li {
    display: flex;
    align-items: center;
    gap: 9px;
    height: 19px;
  }
  .contacts svg { width: 11px; height: 11px; fill: var(--ink); }
  .swoosh {
    position: absolute;
    left: 0;
    bottom: 0;
    width: 520px;
    height: 300px;
  }
  .website {
    font-family: "Roboto", Arial, sans-serif;
    font-size: 11px;
    letter-spacing: 1.4px;
    fill: var(--brand-brown);
  }
</style>
</head>
<body>
<main class="canvas">

  <section class="card card--front" aria-label="Card front">
    <div class="brand">
      <span class="brand__dot"></span>
      <span class="brand__name">Tirovel</span>
    </div>
  </section>

  <section class="card card--back" aria-label="Card back">
    <svg class="swoosh" viewBox="0 0 520 300" aria-hidden="true">
      <path d="M150 300 C 290 262, 420 236, 520 180 L520 300 Z" fill="var(--brand-yellow)"/>
      <path d="M150 300 C 290 256, 420 222, 520 162" fill="none" stroke="var(--brand-brown)" stroke-width="3"/>
      <text class="website" x="300" y="276" transform="rotate(-13 300 276)">www.tirovelgroup.com</text>
    </svg>

    <div class="brand">
      <span class="brand__dot"></span>
      <span class="brand__name">Tirovel</span>
    </div>

    <div class="person">
      <p class="person__name">MARA QUENTLY</p>
      <p class="person__title">Managing Director</p>
    </div>

    <p class="address">214 9th Floor Arcade<br>Harbor Lane KTV</p>

    <ul class="contacts">
      <li>
        <svg viewBox="0 0 12 12"><path d="M2.5 1 L4.5 1 L5.2 3.6 L4 4.6 C4.7 6 6 7.3 7.4 8 L8.4 6.8 L11 7.5 L11 9.5 C11 10.3 10.3 11 9.5 11 C5 11 1 7 1 2.5 C1 1.7 1.7 1 2.5 1 Z"/></svg>
        014 672 3391
      </li>
      <li>
        <svg viewBox="0 0 12 12"><path d="M3.5 0.5 H8.5 A1 1 0 0 1 9.5 1.5 V10.5 A1 1 0 0 1 8.5 11.5 H3.5 A1 1 0 0 1 2.5 10.5 V1.5 A1 1 0 0 1 3.5 0.5 Z M3.7 2 V9 H8.3 V2 Z"/></svg>
        017 208 5546
      </li>
      <li>
        <svg viewBox="0 0 12 12"><path d="M3 1 H8 V4 H3 Z M1 5 H11 V10 H9 V8 H3 V10 H1 Z M3.5 9 H8.5 V11.5 H3.5 Z"/></svg>
        014 672 3390
      </li>
      <li>
        <svg viewBox="0 0 12 12"><path d="M0.5 2.5 H11.5 V9.5 H0.5 Z M1.3 3.2 L6 6.6 L10.7 3.2 Z" fill-rule="evenodd"/></svg>
        hello@tirovel.com
      </li>
    </ul>
  </section>

</main>
</body>
</html>
```